Architecture firm needing a business card

We need a business card design for a new company based in the US called "Dorrance Architecture". Seeking minimalist designs that have a creativity/design feel but must be clean and professional. Please refer to the logo attached.

Target Market(s)

Real Estate Investors, Home Builders and Construction Firms.

Industry/Entity Type

Architecture

Contact Information for Business Card

Standard US size business cards. Would like to have some sort of graphic on the back side of the card - nothing that is too loud but something that may catch your attention. More or less grayscale colors that are in line with the logo colors (navy and greys essentially). Additional colors maybe accepted if blended properly (earthtones), but might be difficult to accomplish and maintain the clean/minimalist look.

Requirements
Must have
• Clean Lines
Nice to have
• some sort of graphics, would like to have something creative on the back side of the card
Should not have
• nothing too busy, cluttered or overwhelming.

```html
<!DOCTYPE html>
<html lang="en">
<head>
<meta charset="utf-8">
<title>Dorrance Architecture – Business Card</title>
<link rel="stylesheet" href="https://fonts.googleapis.com/css2?family=Montserrat:wght@400;600&family=Open+Sans:wght@400;600&display=swap">
<style>
  :root {
    --page: #e4e4e4;
    --navy: #1f4470;
    --navy-deep: #173659;
    --navy-soft: #2a5283;
    --grey: #8c8c8c;
    --grey-light: #f1f1f1;
    --ink: #1f4470;
    --white: #ffffff;
  }
  * { box-sizing: border-box; margin: 0; padding: 0; }
  html, body {
    width: 1200px; height: 1200px; overflow: hidden;
    background: var(--page);
    font-family: "Open Sans", Arial, sans-serif;
  }
  .card {
    position: absolute;
    width: 700px; height: 400px;
    border-radius: 22px;
    overflow: hidden;
    box-shadow: 0 6px 18px rgba(0,0,0,.18);
  }
  /* Back side */
  .card-back {
    left: 170px; top: 170px;
    background: var(--navy);
  }
  .back-pattern {
    position: absolute; inset: 0;
    background: linear-gradient(135deg, var(--navy-soft) 0%, var(--navy) 50%, var(--navy-deep) 100%);
  }
  .back-brand {
    position: absolute; left: 0; right: 0; top: 50%;
    transform: translateY(-50%);
    display: flex; align-items: center; justify-content: center; gap: 22px;
    color: var(--white);
    font-family: "Montserrat", Arial, sans-serif; font-weight: 400;
  }
  .brand-square {
    width: 58px; height: 58px;
    border: 4px solid currentColor;
  }
  .brand-name { line-height: 1; text-transform: uppercase; }
  .brand-name .word-main { display: block; font-size: 50px; letter-spacing: 2px; }
  .brand-name .word-sub { display: block; font-size: 19px; letter-spacing: 5px; margin-top: 8px; }

  /* Front side */
  .card-front {
    left: 330px; top: 630px;
    background: var(--white);
  }
  .front-brand {
    position: absolute; left: 0; top: 0; width: 330px; height: 100%;
    display: flex; flex-direction: column; align-items: center; justify-content: center; gap: 16px;
    color: var(--ink);
    font-family: "Montserrat", Arial, sans-serif; font-weight: 400;
    text-align: center;
  }
  .front-brand .brand-square { width: 54px; height: 54px; }
  .front-brand .word-main { font-size: 42px; letter-spacing: 1px; }
  .front-brand .word-sub { font-size: 16px; letter-spacing: 5px; }
  .divider {
    position: absolute; left: 345px; top: 40px; bottom: 70px;
    width: 1px; background: #e6e6e6;
  }
  .front-decor {
    position: absolute; right: 0; top: 0; width: 260px; height: 300px;
    background: linear-gradient(135deg, var(--grey-light), #fafafa);
  }
  .contact {
    position: absolute; left: 380px; top: 70px; width: 290px;
    color: var(--ink);
  }
  .contact-name {
    font-family: "Montserrat", Arial, sans-serif; font-weight: 600;
    font-size: 23px;
  }
  .contact-title { font-size: 13px; margin: 2px 0 0 20px; }
  .contact-list { list-style: none; margin-top: 24px; font-size: 14px; line-height: 1.5; }
  .contact-list li { display: flex; align-items: flex-start; gap: 12px; }
  .contact-list svg { width: 16px; height: 16px; margin-top: 3px; flex: none; fill: var(--grey); }
  .contact-address { margin-left: 28px; }
  .web-band {
    position: absolute; right: 0; bottom: 0;
    width: 330px; height: 60px;
    background: var(--navy);
    color: var(--white);
    font-size: 15px; letter-spacing: .5px;
    display: flex; align-items: center; justify-content: center;
  }
  .web-band::before {
    content: ""; position: absolute; left: -30px; top: 0;
    border-bottom: 60px solid var(--navy); border-left: 30px solid transparent;
  }
</style>
</head>
<body>

<section class="card card-back">
  <div class="back-pattern" role="img" aria-label="Subtle tone-on-tone repeating brand pattern in navy"></div>
  <div class="back-brand">
    <span class="brand-square"></span>
    <span class="brand-name"><span class="word-main">Dorrance</span><span class="word-sub">Architecture</span></span>
  </div>
</section>

<section class="card card-front">
  <div class="front-decor" role="img" aria-label="Faint oversized brand decoration in light grey"></div>
  <div class="front-brand">
    <span class="brand-square"></span>
    <span class="brand-name"><span class="word-main">Dorrance</span><span class="word-sub">Architecture</span></span>
  </div>
  <div class="divider"></div>
  <div class="contact">
    <p class="contact-name">Your name</p>
    <p class="contact-title">Your Title</p>
    <ul class="contact-list">
      <li>
        <svg viewBox="0 0 16 16" aria-hidden="true"><path d="M3 1h3l1 4-2 1a9 9 0 0 0 5 5l1-2 4 1v3c0 1-1 2-2 2C7 15 1 9 1 3c0-1 1-2 2-2z"/></svg>
        +00 111 222 3333
      </li>
      <li>
        <svg viewBox="0 0 16 16" aria-hidden="true"><path d="M1 3h14v10H1z M2 4l6 5 6-5" fill="none" stroke="#8c8c8c" stroke-width="1.4"/></svg>
        yourname@yourwebsite.com
      </li>
      <li class="contact-address">Your Long Commercial or business address in just two line.</li>
    </ul>
  </div>
  <div class="web-band">www.yourwebsite.com</div>
</section>

</body>
</html>
```